2026 Compostable Stand up Pouch Redesign

Project Overview
We are a natural dog bakery focused on simple, healthy ingredients and earth-friendly packaging. As the first step in a rebrand, we are redesigning our 6 oz stand-up pouch using new compostable packaging materials.
New pouch is the same size and structure as current (template provided)
Files included:
Existing Art template (PDF + JPG)
Photos of current packaging (for reference only)
Copy of existing logo (Meadowlark Treat Kitchen)
Copy of future logo (Birchwood Natural Bakery)
This redesign should feel like a clear upgrade—more refined, more intentional, and more aligned with sustainability.
⚠️ IMPORTANT LAYOUT CONSTRAINT (PLEASE READ)
The new pouch has a full-width horizontal window.
Design elements may ONLY appear above and below the window
No design elements can be placed to the left or right of the window
A 4.5" W x 3.5" H blank space above the window must be preserved
This is reserved for applied product labels
Keep this area completely clean (no textures, patterns, or graphics)
Submissions that ignore these elements will not be considered.
Brand Direction & Style
We are looking for a design that feels:
Natural and ingredient-focused
Eco-conscious and sustainable
Clean and elevated (not rustic, not overly playful)
Warm and trustworthy
Avoid:
Neon or bright artificial colors
Loud, busy, or overly commercial designs
Cartoon-heavy or overly whimsical styles
Color Direction
Our current packaging is kraft brown, but the new material allows full-color printing. We are looking for:
Nature-inspired colors only
Greens, muted blues, warm browns, soft earth tones
Background color is flexible within this palette
Must work with:
Current logo: Meadowlark Treat Kitchen
Future logo: Birchwood Natural Bakery
👉 For this project, use Meadowlark Treat Kitchen logo only
Front of Pouch Requirements
Do NOT include logo on pouch front
(Logo will be on applied labels)
Required Elements
Tagline: Simple, Healthy Ingredients. Earth Friendly Packaging.
Compostable Messaging (REQUIRED):
Must clearly communicate that packaging is compostable
Optional placement:
Tear-off strip near hang hole
BUT must also appear somewhere on the main pouch design
Origin Callout:
“Hand Made in the Pacific Northwest”
Can be a badge, stamp, or graphic (open to redesign)
Icons (Highly Encouraged)
We would like to explore a clean, minimal icon set for:
No Corn
No Wheat
No Soy
No GMOs
Compostable Packaging
(Keep icons simple, clean, and consistent with natural aesthetic)
Back of Pouch Requirements
Messaging Direction
Do NOT use: “The healthiest pet bakery in the US”
Instead, build around:
Simple, Healthy Ingredients. Earth Friendly Packaging.
Content
“Our Recipes” bullet points (from current packaging – still valid)
Sustainability messaging:
Include reference to reducing our “carbon pawprint”
Emphasize eco-friendly materials and practices
Design Direction
Open to new layout and graphics
Should visually reinforce:
Clean ingredients
Natural sourcing
Sustainability
Printing Considerations
Design should be mindful of production scalability:
Should translate well to both digital and roto printing
Avoid overly complex gradients or excessive color layering
Creative Freedom (Important)
While we have outlined structure and constraints, we are intentionally leaving visual interpretation open.
We welcome:
Fresh layout ideas
Refined graphic elements
Elevated visual storytelling
We are especially interested in designs that feel:
Thoughtful
Clean
Naturally premium
Any design submission that includes loud, neon, or "aggressive" color schemes or a mass market appeal will be eliminated immediately. We are a premium, natural dog bakery found in independent stores only.
UPDATED & IMPORTANT DESIGN REQUIREMENTS (PLEASE READ)
This pouch is a base design used across all flavors. A separate product label will be applied.
A clearly defined blank area must be left for label placement (do not incorporate into artwork).
The product viewing window is fixed:
Size and placement must match the template exactly
Do not resize, reposition, or redesign the window
Designs that do not follow these requirements will not be considered.
Please review the discussion board for additional feedback and direction before submitting revisions.

```html
<!DOCTYPE html>
<html lang="en">
<head>
<meta charset="utf-8">
<title>Meadowlark Treat Kitchen – Compostable Stand-up Pouch Dieline</title>
<link href="https://fonts.googleapis.com/css2?family=Cormorant+Garamond:wght@400;500&family=Source+Serif+4:wght@400;600;700&family=DM+Sans:wght@400;500;700&display=swap" rel="stylesheet">
<style>
  :root {
    --pouch-navy: #2b4c6e;
    --pattern-tone: #335a80;
    --dim-blue: #1aa3e0;
    --rule-blue: #1d7cc4;
    --label-sage: #a7b29c;
    --window-grey: #bdbec0;
    --cream: #ebe4cf;
    --bleed-red: #e8505b;
    --arrow-brown: #a88a64;
    --ink: #1b1b1b;
    --stamp-ink: #2f3d2a;
  }
  html, body { margin: 0; padding: 0; width: 1200px; height: 2161px; overflow: hidden; background: #ffffff; }
  .dieline { display: block; width: 1200px; height: 2161px; }
  .dim-text { font-family: "DM Sans", sans-serif; font-size: 8.5px; fill: var(--dim-blue); }
  .dim-label { font-family: "DM Sans", sans-serif; font-weight: 700; font-size: 16px; fill: var(--rule-blue); }
  .dim-line { stroke: var(--dim-blue); stroke-width: 1; fill: none; }
  .tagline-small { font-family: "Cormorant Garamond", serif; font-size: 15px; fill: var(--cream); }
  .icon-caption { font-family: "Source Serif 4", serif; font-size: 7.5px; fill: var(--cream); }
  .icon-stroke { fill: none; stroke: var(--cream); stroke-width: 1; stroke-linecap: round; stroke-linejoin: round; }
  .window-note { font-family: "DM Sans", sans-serif; font-size: 9px; fill: var(--dim-blue); }
  .origin-text { font-family: "DM Sans", sans-serif; font-size: 9px; fill: var(--cream); letter-spacing: .3px; }
  .back-headline { font-family: "Source Serif 4", serif; font-weight: 600; font-size: 24px; fill: var(--cream); }
  .section-title { font-family: "Source Serif 4", serif; font-weight: 600; font-size: 18px; fill: var(--cream); }
  .recipe-item { font-family: "Source Serif 4", serif; font-size: 10px; fill: var(--cream); }
  .body-small { font-family: "DM Sans", sans-serif; font-size: 7.5px; fill: var(--cream); }
  .company-name { font-family: "Source Serif 4", serif; font-weight: 700; font-size: 10px; letter-spacing: .8px; fill: var(--cream); }
  .company-detail { font-family: "Source Serif 4", serif; font-size: 8px; fill: var(--cream); }
  .stamp-text { font-family: "Source Serif 4", serif; font-size: 13px; letter-spacing: .8px; fill: var(--stamp-ink); }
  .notice-text { font-family: "Source Serif 4", serif; font-size: 8.3px; fill: var(--stamp-ink); }
  .annotation { font-family: "DM Sans", sans-serif; font-size: 12px; fill: var(--ink); }
  .logo-word { font-family: "Source Serif 4", serif; font-weight: 600; font-size: 17px; fill: #2f5a32; }
</style>
</head>
<body>
<svg class="dieline" viewBox="0 0 1024 1844" xmlns="http://www.w3.org/2000/svg" aria-label="Stand-up pouch dieline">
  <defs>
    <linearGradient id="meadow" x1="0" y1="0" x2="0" y2="1">
      <stop offset="0" stop-color="#8aa765"/>
      <stop offset="1" stop-color="#4d7a3a"/>
    </linearGradient>
    <linearGradient id="backMeadow" x1="0" y1="0" x2="0" y2="1">
      <stop offset="0" stop-color="#6f8a74"/>
      <stop offset=".45" stop-color="#668f49"/>
      <stop offset="1" stop-color="#4d7a38"/>
    </linearGradient>
    <marker id="arrowHead" markerWidth="10" markerHeight="10" refX="6" refY="5" orient="auto">
      <path d="M0 1 L7 5 L0 9" fill="none" stroke="var(--arrow-brown)" stroke-width="1.5"/>
    </marker>
  </defs>

  <g class="dim-width">
    <line class="dim-line" x1="313" y1="74" x2="737" y2="74"/>
    <line class="dim-line" x1="313" y1="67" x2="313" y2="81"/>
    <line class="dim-line" x1="737" y1="67" x2="737" y2="81"/>
    <text class="dim-text" x="525" y="63" text-anchor="middle">150.00 mm (5.91 in)</text>
  </g>

  <g class="dim-height">
    <line class="dim-line" x1="232" y1="110" x2="232" y2="1668"/>
    <line class="dim-line" x1="224" y1="110" x2="240" y2="110"/>
    <line class="dim-line" x1="224" y1="1668" x2="240" y2="1668"/>
    <text class="dim-text" transform="translate(219 889) rotate(-90)" text-anchor="middle">550.00 mm (21.65 in)</text>
    <line class="dim-line" x1="270" y1="110" x2="270" y2="1668"/>
    <line class="dim-line" x1="262" y1="110" x2="278" y2="110"/>
    <line class="dim-line" x1="262" y1="762" x2="278" y2="762"/>
    <line class="dim-line" x1="262" y1="1017" x2="278" y2="1017"/>
    <line class="dim-line" x1="262" y1="1668" x2="278" y2="1668"/>
    <text class="dim-text" transform="translate(258 436) rotate(-90)" text-anchor="middle">230.00 mm (9.06 in)</text>
    <text class="dim-text" transform="translate(258 889) rotate(-90)" text-anchor="middle">90.00 mm (3.54 in)</text>
    <text class="dim-text" transform="translate(258 1342) rotate(-90)" text-anchor="middle">230.00 mm (9.06 in)</text>
  </g>

  <g class="front-panel">
    <rect role="img" aria-label="Diagonal line pattern border" x="312" y="107" width="425" height="655" rx="10" fill="var(--pattern-tone)"/>
    <path d="M330 107 H719 V628 C700 700 620 752 530 752 C440 752 360 715 330 660 Z" fill="var(--pouch-navy)"/>
    <line x1="312" y1="167" x2="737" y2="167" stroke="var(--rule-blue)" stroke-width=".8" stroke-dasharray="3 3"/>
    <line x1="312" y1="196" x2="737" y2="196" stroke="var(--rule-blue)" stroke-width="3"/>
    <line x1="330" y1="210" x2="719" y2="210" stroke="var(--rule-blue)" stroke-width=".8" stroke-dasharray="3 3"/>
    <circle cx="316" cy="167" r="4" fill="var(--label-sage)"/>
    <circle cx="733" cy="167" r="4" fill="var(--label-sage)"/>

    <rect class="label-area" x="366" y="219" width="324" height="252" fill="var(--label-sage)"/>

    <text class="tagline-small" x="529" y="493" text-anchor="middle">Simple, Healthy Ingredients. Earth Friendly Packaging.</text>

    <g class="free-from-icons">
      <path class="icon-stroke" d="M346 525 C346 508 360 502 368 502 C368 515 360 525 346 525 Z M346 525 L362 509"/>
      <text class="icon-caption" x="373" y="517">No GMOs</text>
      <line x1="416" y1="500" x2="416" y2="528" stroke="var(--cream)" stroke-width=".5" opacity=".5"/>
      <path class="icon-stroke" d="M424 524 C430 508 448 500 458 506 C454 518 438 528 424 524 Z"/>
      <circle cx="437" cy="516" r="2.5" class="icon-stroke"/><circle cx="445" cy="511" r="2.5" class="icon-stroke"/>
      <text class="icon-caption" x="463" y="517">No Soy</text>
      <line x1="495" y1="500" x2="495" y2="528" stroke="var(--cream)" stroke-width=".5" opacity=".5"/>
      <path class="icon-stroke" d="M512 528 V502 M512 510 C506 508 505 503 506 500 M512 510 C518 508 519 503 518 500 M512 518 C506 516 505 511 506 508 M512 518 C518 516 519 511 518 508"/>
      <text class="icon-caption" x="523" y="517">No Wheat</text>
      <line x1="567" y1="500" x2="567" y2="528" stroke="var(--cream)" stroke-width=".5" opacity=".5"/>
      <path class="icon-stroke" d="M585 528 C579 518 579 506 585 498 C591 506 591 518 585 528 Z M578 528 C576 520 578 514 581 512 M592 528 C594 520 592 514 589 512"/>
      <text class="icon-caption" x="595" y="517">No Corn</text>
      <line x1="632" y1="500" x2="632" y2="528" stroke="var(--cream)" stroke-width=".5" opacity=".5"/>
      <path class="icon-stroke" d="M640 512 L650 506 L660 512 V522 L650 528 L640 522 Z M640 512 L650 518 L660 512 M650 518 V528"/>
      <text class="icon-caption" x="665" y="511">packaging</text>
      <text class="icon-caption" x="665" y="521">compostable</text>
    </g>

    <rect class="product-window" x="401" y="544" width="256" height="91" rx="4" fill="var(--window-grey)"/>
    <text class="window-note" x="525" y="580" text-anchor="middle">90.00 mm w</text>
    <text class="window-note" x="525" y="592" text-anchor="middle">x</text>
    <text class="window-note" x="525" y="604" text-anchor="middle">32.00 mm h</text>

    <path role="img" aria-label="Illustrated green hills with evergreen trees and a Hand Made in the Pacific Northwest badge" d="M378 690 C420 650 500 640 540 655 C600 640 680 645 705 668 C680 715 610 750 535 750 C460 750 400 730 378 690 Z" fill="url(#meadow)"/>
    <text class="origin-text" x="536" y="696" text-anchor="middle">Hand Made in</text>
    <text class="origin-text" x="536" y="709" text-anchor="middle">the Pacific Northwest</text>
  </g>

  <g class="gusset-panel">
    <rect role="img" aria-label="Diagonal line pattern border" x="312" y="763" width="425" height="254" rx="10" fill="var(--pattern-tone)"/>
    <path d="M330 888 C380 810 460 785 530 785 C610 785 680 820 719 888 C680 958 610 992 530 992 C450 992 380 965 330 888 Z" fill="var(--pouch-navy)"/>
    <line x1="305" y1="888" x2="745" y2="888" stroke="var(--rule-blue)" stroke-width=".6" stroke-dasharray="3 3"/>
  </g>

  <g class="back-panel">
    <rect role="img" aria-label="Diagonal line pattern border" x="312" y="1018" width="425" height="650" rx="10" fill="var(--pattern-tone)"/>
    <path d="M330 1668 V1110 C380 1060 460 1035 530 1035 C610 1035 690 1070 719 1110 V1668 Z" fill="var(--pouch-navy)"/>

    <text class="back-headline" x="530" y="1119" text-anchor="middle">Simple, Healthy Ingredients.</text>
    <text class="back-headline" x="530" y="1149" text-anchor="middle">Earth Friendly Packaging.</text>

    <path role="img" aria-label="Layered green meadow landscape" d="M330 1295 C400 1275 470 1280 540 1295 C610 1300 680 1285 720 1290 V1410 C620 1402 520 1410 420 1404 C380 1402 350 1404 330 1400 Z" fill="url(#backMeadow)"/>

    <path class="plain-badge" d="M350 1215 C370 1200 400 1205 412 1190 C430 1182 470 1188 486 1205 C488 1225 480 1250 470 1262 C450 1280 410 1282 380 1278 C360 1276 346 1268 350 1250 C344 1235 342 1225 350 1215 Z" fill="var(--label-sage)"/>

    <text class="section-title" x="555" y="1212">Our Recipes</text>
    <g class="recipe-list">
      <path class="icon-stroke" d="M551 1232 H577 C577 1240 570 1244 564 1244 C558 1244 551 1240 551 1232 Z M556 1228 L558 1226 M564 1225 V1222 M571 1228 L569 1226"/>
      <text class="recipe-item" x="588" y="1237">clean &amp; simple</text>
      <path class="icon-stroke" d="M558 1248 V1258 L551 1270 H573 L566 1258 V1248 Z M553 1270 L573 1246"/>
      <text class="recipe-item" x="588" y="1258">nothing artifical</text>
      <path class="icon-stroke" d="M550 1284 H572 V1296 C572 1300 568 1301 561 1301 C554 1301 550 1300 550 1296 Z M546 1286 H550 M572 1286 H576 M580 1292 L586 1281"/>
      <text class="recipe-item" x="591" y="1288">handcrafted in small</text>
      <text class="recipe-item" x="591" y="1300">batches</text>
      <path class="icon-stroke" d="M547 1326 C550 1316 562 1314 570 1320 C574 1326 570 1334 560 1334 C552 1334 547 1330 547 1326 Z M566 1318 C568 1310 574 1308 576 1310"/>
      <text class="recipe-item" x="591" y="1324">premium ingredients</text>
    </g>

    <g class="eco-stamp">
      <rect x="352" y="1325" width="112" height="45" fill="var(--label-sage)" stroke="#3b4a36" stroke-width="1" stroke-dasharray="3 2"/>
      <path d="M378 1341 C378 1334 384 1331 388 1331 C388 1337 384 1341 378 1341 Z" fill="#4f7a3a"/>
      <text class="stamp-text" x="394" y="1343">ECO</text>
      <text class="stamp-text" x="366" y="1361">FRIENDLY</text>
    </g>

    <text class="section-title" x="352" y="1416">Sustainability</text>
    <path class="icon-stroke" d="M472 1415 C472 1405 478 1400 486 1399 C486 1409 480 1414 472 1415 Z M470 1420 L480 1407"/>
    <text class="body-small" x="355" y="1429">We are committed to reducing our</text>
    <text class="body-small" x="355" y="1439">carbon pawprint</text>
    <text class="body-small" x="355" y="1449">through responsible sourcing and</text>
    <text class="body-small" x="355" y="1459">compostable packaging</text>

    <text class="company-name" x="539" y="1428">MEADOWLARK TREAT KITCHEN</text>
    <text class="company-detail" x="539" y="1441">Alder Cove, WA | 555-201-BAKE</text>
    <text class="company-detail" x="539" y="1453">www.meadowlarktreatkitchen.com</text>

    <g class="compost-notice">
      <rect x="393" y="1475" width="280" height="78" fill="var(--label-sage)" stroke="#3b4a36" stroke-width="1" stroke-dasharray="3 2"/>
      <text class="notice-text" x="401" y="1507">OUR FOCUS IS ON REDUCING OUR CARBON PAWPRINT.</text>
      <text class="notice-text" x="401" y="1519">THIS PACKAGE IS MADE FROM</text>
      <text class="notice-text" x="403" y="1531">MATERIALS TAHT ARE 100% home compostable.</text>
    </g>

    <line x1="312" y1="1576" x2="737" y2="1576" stroke="var(--rule-blue)" stroke-width="3"/>
    <line x1="330" y1="1590" x2="719" y2="1590" stroke="var(--rule-blue)" stroke-width=".8" stroke-dasharray="3 3"/>
    <line x1="312" y1="1612" x2="737" y2="1612" stroke="var(--rule-blue)" stroke-width=".8" stroke-dasharray="3 3"/>
    <circle cx="316" cy="1612" r="4" fill="var(--label-sage)"/>
    <circle cx="733" cy="1612" r="4" fill="var(--label-sage)"/>
  </g>

  <rect x="330" y="93" width="454" height="1587" fill="none" stroke="var(--bleed-red)" stroke-width=".8"/>

  <g class="dim-right">
    <line class="dim-line" x1="793" y1="110" x2="793" y2="167"/>
    <line class="dim-line" x1="787" y1="110" x2="799" y2="110"/>
    <line class="dim-line" x1="787" y1="167" x2="799" y2="167"/>
    <text class="dim-label" transform="translate(784 162) rotate(-90)">TEAR</text>
    <text class="dim-text" transform="translate(809 180) rotate(-90)">20.00 mm (0.79 in)</text>
    <line class="dim-line" x1="843" y1="110" x2="843" y2="207"/>
    <line class="dim-line" x1="837" y1="110" x2="849" y2="110"/>
    <line class="dim-line" x1="837" y1="207" x2="849" y2="207"/>
    <text class="dim-label" transform="translate(834 186) rotate(-90)">ZIPPER</text>
    <text class="dim-text" transform="translate(859 203) rotate(-90)">35.00 mm (1.38 in)</text>

    <line class="dim-line" x1="788" y1="544" x2="788" y2="635"/>
    <line class="dim-line" x1="782" y1="544" x2="794" y2="544"/>
    <line class="dim-line" x1="782" y1="635" x2="794" y2="635"/>
    <text class="dim-label" transform="translate(774 628) rotate(-90)">WINDOW</text>
    <text class="dim-text" transform="translate(806 632) rotate(-90)">32.00 mm (1.26 in)</text>

    <line class="dim-line" x1="780" y1="763" x2="780" y2="1017"/>
    <line class="dim-line" x1="774" y1="763" x2="786" y2="763"/>
    <line class="dim-line" x1="774" y1="888" x2="786" y2="888"/>
    <line class="dim-line" x1="774" y1="1017" x2="786" y2="1017"/>
    <text class="dim-text" transform="translate(801 868) rotate(-90)">45.00 mm (1.77 in)</text>
    <text class="dim-text" transform="translate(801 995) rotate(-90)">45.00 mm (1.77 in)</text>
  </g>

  <g class="label-callout">
    <text class="annotation" x="820" y="293">A 4.5" W x 3.5" H blank space</text>
    <path d="M860 312 C780 290 690 310 630 358" fill="none" stroke="var(--arrow-brown)" stroke-width="1.6" marker-end="url(#arrowHead)"/>
    <rect x="798" y="325" width="216" height="91" fill="var(--label-sage)"/>
    <text class="logo-word" x="906" y="376" text-anchor="middle">Meadowlark Treat Kitchen</text>
  </g>
</svg>
</body>
</html>
```